Harvesting Victors 6x9 book soft cover- front cover only

We need a book cover for a softcover book. We will need final files in Photoshop or InDesign is preferred.

Overall Title:
Harvesting Victors
Subtitle:
The Foundations of Humble Mentoring for Trainers, Instructors and Players
Author:
by Dr. Marcus Pettiford

The audience is high school and college coaches however we don't want the standard picture with words over the top. Make it a creative design but keep it mind it's a little academic.

```html
<!DOCTYPE html>
<html lang="en">
<head>
<meta charset="utf-8">
<title>Harvesting Victors — Front Cover</title>
<link href="https://fonts.googleapis.com/css2?family=Anton&family=Oswald:wght@400;500&display=swap" rel="stylesheet">
<style>
  :root {
    --backdrop: #2f2f2f;
    --paper: #ffffff;
    --ink: #111111;
    --accent: #ff0000;
    --type-heavy: "Anton", "Impact", sans-serif;
    --type-condensed: "Oswald", "Arial Narrow", sans-serif;
  }
  * { box-sizing: border-box; margin: 0; padding: 0; }
  html, body {
    width: 1200px;
    height: 1200px;
    overflow: hidden;
    background: var(--backdrop);
  }
  .cover {
    position: absolute;
    left: 240px;
    top: 60px;
    width: 720px;
    height: 1080px;
    background: var(--paper);
    overflow: hidden;
  }
  .title-art {
    position: absolute;
    inset: 0;
    width: 720px;
    height: 1080px;
  }
  .title-word {
    font-family: var(--type-heavy);
    font-weight: 400;
  }
  .title-word--lead { fill: var(--ink); font-size: 325px; }
  .title-word--accent { fill: var(--accent); font-size: 320px; }
  .author-name {
    font-family: var(--type-condensed);
    font-weight: 400;
    font-size: 40px;
    letter-spacing: 0.04em;
    fill: var(--ink);
  }
  .athlete-figure {
    position: absolute;
    left: 548px;
    top: 200px;
    width: 78px;
    height: 226px;
    border-radius: 36px 36px 16px 16px;
    background: linear-gradient(180deg, #1a1a1a, #000000);
  }
  .subtitle {
    position: absolute;
    left: 0;
    right: 0;
    top: 942px;
    text-align: center;
    font-family: var(--type-condensed);
    font-weight: 500;
    font-size: 24px;
    line-height: 1.4;
    letter-spacing: 0.12em;
    color: var(--ink);
    text-transform: uppercase;
  }
  .subtitle span { display: block; }
</style>
</head>
<body>
  <main class="cover">
    <svg class="title-art" viewBox="0 0 720 1080" aria-label="Harvesting Victors by Dr. Marcus Pettiford">
      <text class="title-word title-word--lead" transform="rotate(-90)" x="-925" y="356"
            textLength="878" lengthAdjust="spacingAndGlyphs">HARVESTING</text>
      <text class="title-word title-word--accent" transform="rotate(-90)" x="-905" y="658"
            textLength="790" lengthAdjust="spacingAndGlyphs">VICTORS</text>
      <text class="author-name" x="382" y="112"
            textLength="276" lengthAdjust="spacingAndGlyphs">DR. MARCUS PETTIFORD</text>
    </svg>

    <div class="athlete-figure" role="img" aria-label="Black silhouette of a leaping athlete raising a trophy overhead"></div>

    <h2 class="subtitle">
      <span>The Foundations of Humble Mentoring for</span>
      <span>Trainers, Instructors and Players</span>
    </h2>
  </main>
</body>
</html>
```